Business card and stationery design

Harbour & Summit Planners is a leading event and conference design and management company.
Please view harbourandsummit.com.au

The business cards needs to convey:
- professionalism and competency
- exclusivity
- memorable experiences and quality

The business card needs to have the following aspects:
- double sided
- Full colour CMYK
- Printed on either high gloss matt card (designer to recommend)

For the business stationery we require:
- Letterhead with top banner and bottom footer
- A thank you card design
- a with compliments slip design
- a MS powerpoint and MS publisher client presentation slide design which includes cover page and then a standard presentation page
(Note- we do NOT require an envelope design- who sends letters these days!)

The company image is using the key colours of gold, silver and black.
A black background to the business card has been used before and is preferred although we are open to options.

Target Market(s)

High end corporations and businesses that require their events and conferences to be exceptionally well designed and managed

Industry/Entity Type

Business

Contact Information for Business Card

FRONT:

Darcy Whitlam
- Event and Conference Specialist

Mobile- +61 (0) 491 362 047
Office- 1300 586 917
darcyw@harbourandsummit.com.au

Web- harbourandsummit.com.au

BACK:

- Event and

Font styles to use
Other font styles liked:
• The logo designer used Trajan Pro Bold 3 for the font text in the logo

Requirements
Must have
• Amazing design of the following:
• - business card (double sided)
• - letterhead
• - client thank you card
• - powerpoint and publisher client presentation design files

```html
<!DOCTYPE html>
<html lang="en">
<head>
<meta charset="utf-8">
<title>Harbour &amp; Summit Planners — Business Card</title>
<link rel="stylesheet" href="https://fonts.googleapis.com/css2?family=Cinzel:wght@600&family=Open+Sans:wght@400&display=swap">
<style>
  :root {
    --backdrop: #d9d9d9;
    --card-black: #121212;
    --card-black-soft: #2b2b2b;
    --gold: #c9a86a;
    --silver: #dcdcdc;
    --text-grey: #c4c4c4;
    --pattern-light: #f2f2f2;
    --pattern-mid: #bdbdbd;
    --pattern-deep: #5e5e5e;
    --pattern-dark: #2e2e2e;
  }
  * { margin: 0; padding: 0; box-sizing: border-box; }
  html, body {
    width: 1200px;
    height: 900px;
    overflow: hidden;
    background: var(--backdrop);
  }
  .canvas {
    position: relative;
    width: 1200px;
    height: 900px;
  }
  .business-card {
    position: absolute;
    left: 180px;
    top: 195px;
    width: 840px;
    height: 510px;
    background: linear-gradient(100deg, var(--card-black-soft) 0%, var(--card-black) 55%);
    overflow: hidden;
    box-shadow: 0 6px 18px rgba(0,0,0,0.25);
  }
  .pattern-panel {
    position: absolute;
    right: 0;
    top: 0;
    width: 470px;
    height: 510px;
  }
  .brand {
    position: absolute;
    left: 55px;
    top: 46px;
    width: 340px;
    display: flex;
    flex-direction: column;
    align-items: center;
    gap: 24px;
  }
  .brand-mark {
    width: 112px;
    height: 112px;
    border-radius: 50%;
    background: var(--gold);
  }
  .brand-name {
    font-family: 'Cinzel', serif;
    font-weight: 600;
    font-size: 25px;
    line-height: 1.2;
    color: var(--silver);
    text-align: center;
    letter-spacing: 0.5px;
  }
  .holder {
    position: absolute;
    left: 60px;
    top: 288px;
  }
  .holder-name {
    font-family: 'Cinzel', serif;
    font-weight: 600;
    font-size: 26px;
    color: var(--gold);
    letter-spacing: 1px;
  }
  .holder-role {
    font-family: 'Open Sans', sans-serif;
    font-size: 16px;
    color: var(--text-grey);
    margin-top: 0;
    letter-spacing: 0.5px;
  }
  .contact-list {
    position: absolute;
    left: 60px;
    top: 368px;
    list-style: none;
    font-family: 'Open Sans', sans-serif;
    font-size: 16px;
    color: var(--text-grey);
    letter-spacing: 0.4px;
  }
  .contact-item {
    display: flex;
    align-items: center;
    gap: 10px;
    height: 28px;
  }
  .contact-icon {
    width: 15px;
    height: 15px;
    fill: var(--gold);
    flex: none;
  }
</style>
</head>
<body>
<main class="canvas">
  <article class="business-card">
    <svg class="pattern-panel" viewBox="0 0 470 510" role="img" aria-label="Decorative black and white dotted spiral pattern">
      <defs>
        <radialGradient id="panelTone" cx="78%" cy="52%" r="78%">
          <stop offset="0" stop-color="var(--pattern-light)"/>
          <stop offset="0.22" stop-color="var(--pattern-light)"/>
          <stop offset="0.45" stop-color="var(--pattern-mid)"/>
          <stop offset="0.75" stop-color="var(--pattern-deep)"/>
          <stop offset="1" stop-color="var(--pattern-dark)"/>
        </radialGradient>
      </defs>
      <path d="M160 0 C 90 50, 30 130, 10 230 C -5 320, 40 430, 110 510 L 470 510 L 470 0 Z" fill="url(#panelTone)"/>
      <path d="M160 0 C 90 50, 30 130, 10 230 C -5 320, 40 430, 110 510" fill="none" stroke="var(--pattern-light)" stroke-width="6"/>
    </svg>

    <header class="brand">
      <div class="brand-mark" aria-hidden="true"></div>
      <h1 class="brand-name">Harbour &amp; Summit Planners</h1>
    </header>

    <section class="holder">
      <h2 class="holder-name">Darcy Whitlam</h2>
      <p class="holder-role">Event and Conference Specialist</p>
    </section>

    <ul class="contact-list">
      <li class="contact-item">
        <svg class="contact-icon" viewBox="0 0 16 16" aria-hidden="true"><path d="M3.5 1 6 3.5 4.6 5.4c.9 2 2.4 3.6 4.4 4.6L10.7 8.6 13.9 11l-1.6 2.9C6.8 13.5 2.3 9 2 3.5z"/></svg>
        <span>+61 (0) 491 362 047</span>
      </li>
      <li class="contact-item">
        <svg class="contact-icon" viewBox="0 0 16 16" aria-hidden="true"><path d="M3.5 1 6 3.5 4.6 5.4c.9 2 2.4 3.6 4.4 4.6L10.7 8.6 13.9 11l-1.6 2.9C6.8 13.5 2.3 9 2 3.5z"/></svg>
        <span>1300 586 917</span>
      </li>
      <li class="contact-item">
        <svg class="contact-icon" viewBox="0 0 16 16" aria-hidden="true"><path d="M1 3h14v10H1z M2 4l6 5 6-5" stroke="var(--card-black)" stroke-width="1"/></svg>
        <span>darcyw@harbourandsummit.com.au</span>
      </li>
      <li class="contact-item">
        <svg class="contact-icon" viewBox="0 0 16 16" aria-hidden="true"><circle cx="8" cy="8" r="7"/><path d="M1 8h14M8 1c-3 4-3 10 0 14M8 1c3 4 3 10 0 14" stroke="var(--card-black)" stroke-width="1" fill="none"/></svg>
        <span>harbourandsummit.com.au</span>
      </li>
    </ul>
  </article>
</main>
</body>
</html>
```